New Web Design Project

See attachments on the content and concept. Very important that the flow of the tiers stand out

Target Market(s)

Food and Beverage Manufacturing

Industry/Entity Type

Food and Beverage

Coding

Coded - Design and coding required

Number of Pages Required

3 page

Colors
0054AA
0677BA
7BADD7
CADEEF
E8F1F8

```html
<!DOCTYPE html>
<html lang="en">
<head>
<meta charset="utf-8">
<title>Northgate Assurance Group — SQF Consulting</title>
<link href="https://fonts.googleapis.com/css2?family=Libre+Baskerville:wght@400;700&family=Outfit:wght@300;400;500;600&display=swap" rel="stylesheet">
<style>
:root{
  --blue-deep:#0054AA;
  --blue:#0677BA;
  --blue-soft:#7BADD7;
  --blue-pale:#CADEEF;
  --blue-mist:#E8F1F8;
  --navy:#0B2A5B;
  --navy-dark:#08214A;
  --ink:#0E2A55;
  --text:#3B4A60;
  --white:#ffffff;
  --green:#2FA84F;
  --star:#F5A623;
}
*{margin:0;padding:0;box-sizing:border-box}
html,body{width:1200px;height:3705px;overflow:hidden}
body{position:relative;background:var(--white);font-family:'Outfit',sans-serif;color:var(--text)}
.abs{position:absolute}
.serif{font-family:'Libre Baskerville',serif;font-weight:700;text-transform:uppercase;color:var(--ink)}
.eyebrow{font-size:11px;font-weight:600;letter-spacing:.3px;color:var(--ink);text-transform:uppercase}
.center{left:0;width:1200px;text-align:center}
.btn{display:flex;align-items:center;justify-content:center;border-radius:24px;font-size:13px;font-weight:500}

/* nav */
.nav{top:0;left:0;width:1200px;height:83px;background:var(--white)}
.brand{display:flex;align-items:center;gap:8px}
.brand-dot{width:34px;height:34px;border-radius:50%;border:2.5px solid var(--navy)}
.brand-name{font-family:'Libre Baskerville',serif;font-weight:700;font-size:18px;color:var(--navy)}
.brand-sub{font-size:9px;letter-spacing:1px;color:var(--navy)}
.nav-link{top:33px;font-size:12px;color:var(--text)}
.nav-btn{left:905px;top:18px;width:182px;height:46px;background:var(--blue-deep);color:var(--white)}

/* hero */
.hero{top:83px;left:0;width:1200px;height:594px;background:linear-gradient(90deg,#33404d 0%,#6d7a86 45%,#b9c4cd 70%,#556b8a 100%)}
.hero-shade{top:83px;left:0;width:700px;height:594px;background:linear-gradient(90deg,rgba(20,28,38,.55),rgba(20,28,38,0))}
.hero-eyebrow{left:115px;top:206px;font-size:11px;font-weight:600;color:var(--white)}
.hero-title{left:115px;top:234px;font-size:30px;line-height:45px;color:var(--white)}
.hero-copy{left:115px;top:418px;width:480px;font-size:12px;line-height:19px;color:var(--white)}
.hero-btn{left:115px;top:494px;width:182px;height:46px;background:var(--blue-deep);color:var(--white)}

/* stats */
.stats-band{top:677px;left:0;width:1200px;height:190px}
.stat{top:717px;width:200px;text-align:center;color:var(--white)}
.stat-num{font-family:'Libre Baskerville',serif;font-size:34px;font-weight:700;line-height:46px}
.stat-label{font-size:11px;margin-top:2px}
.stat-divider{top:697px;width:1px;height:100px;background:rgba(255,255,255,.25)}

/* services */
.section-title{font-size:26px;line-height:33px}
.lead{font-size:12px;line-height:19px;color:var(--text)}
.card{top:1123px;width:312px;height:222px;border:1.5px solid var(--blue);border-radius:16px;text-align:center;padding:16px 24px 0}
.card svg{display:block;margin:0 auto}
.card-title{font-family:'Libre Baskerville',serif;font-weight:700;font-size:14px;color:var(--ink);text-transform:uppercase;margin-top:16px}
.card-text{font-size:12px;line-height:18px;margin-top:8px;color:var(--text)}
.dots{display:flex;gap:7px;justify-content:center}
.dots span{width:11px;height:11px;border-radius:50%;background:var(--blue-pale)}
.dots span.on{background:var(--blue-deep)}

/* why */
.why{top:1486px;left:0;width:1200px;height:691px;background:var(--blue-mist)}
.benefit{left:570px;width:470px}
.benefit-title{display:flex;align-items:center;gap:8px;font-family:'Libre Baskerville',serif;font-weight:700;font-size:13.5px;color:var(--ink);text-transform:uppercase}
.benefit-text{margin-left:21px;margin-top:4px;font-size:11.5px;line-height:18px;color:var(--text)}

/* steps */
.step{top:2376px;width:267px;height:232px;border:1.5px solid var(--blue);border-radius:16px;text-align:center;padding:18px 22px 0}
.step svg{display:block;margin:0 auto}
.step-featured{background:linear-gradient(160deg,var(--blue-deep),var(--blue));border:none}
.step-featured .card-title,.step-featured .card-text{color:var(--white)}

/* quote */
.quote-mark{top:2725px;font-family:'Libre Baskerville',serif;font-size:110px;line-height:110px;color:var(--blue-deep)}
.quote{top:2808px;left:230px;width:740px;text-align:center;font-size:20px;line-height:30px}
.stars{top:2937px;color:var(--star);font-size:19px;letter-spacing:1px}
.quote-by{top:2977px;font-size:11px;font-weight:600;color:var(--ink)}

/* cta */
.cta{top:3090px;left:0;width:1200px;height:191px}
.cta-title{left:115px;top:3168px;font-size:30px;color:var(--white)}
.cta-copy{left:115px;top:3217px;width:520px;font-size:12px;line-height:19px;color:var(--white)}
.cta-btn{left:906px;top:3192px;width:181px;height:45px;background:var(--white);color:var(--blue-deep)}

/* footer */
.footer{top:3281px;left:0;width:1200px;height:424px;background:var(--navy)}
.footer-base{top:3650px;left:0;width:1200px;height:55px;background:var(--navy-dark)}
.footer .brand-name,.footer-brand .brand-name{color:var(--white)}
.footer-about{left:115px;top:3470px;width:290px;font-size:11.5px;line-height:19px;color:var(--blue-pale)}
.col-title{top:3358px;font-family:'Libre Baskerville',serif;font-weight:700;font-size:19px;color:var(--white);text-transform:uppercase}
.svc-list{left:464px;top:3403px;list-style:none}
.svc-list li{display:flex;align-items:center;gap:8px;font-size:11.5px;color:var(--blue-pale);height:23.7px}
.contact{left:697px;width:230px}
.contact-head{display:flex;align-items:center;gap:10px;font-family:'Libre Baskerville',serif;font-weight:700;font-size:12.5px;color:var(--white);text-transform:uppercase}
.contact-text{margin-left:21px;margin-top:4px;font-size:11.5px;line-height:19px;color:var(--blue-pale)}
.social{width:34px;height:34px;border-radius:50%;background:rgba(255,255,255,.1);border:1px solid rgba(255,255,255,.2)}
.copyright{top:3669px;font-size:11.5px;color:var(--white)}
.chat{left:1114px;top:3619px;width:52px;height:52px;border-radius:50%;background:var(--blue);display:flex;align-items:center;justify-content:center}
</style>
</head>
<body>

<!-- Navigation -->
<header class="abs nav">
  <div class="abs brand" style="left:113px;top:22px">
    <span class="brand-dot"></span>
    <div>
      <div class="brand-name">Northgate Assurance</div>
      <div class="brand-sub">FOOD SAFETY &amp; SQF CERTIFICATION</div>
    </div>
  </div>
  <span class="abs nav-link" style="left:523px">Services</span>
  <span class="abs nav-link" style="left:610px">Benefits</span>
  <span class="abs nav-link" style="left:697px">Process</span>
  <span class="abs nav-link" style="left:781px">Contact Us</span>
  <svg class="abs" style="left:863px;top:31px" width="20" height="20" viewBox="0 0 20 20"><path d="M14 14.5A7 7 0 0 1 8 3a7 7 0 1 0 9 9 7 7 0 0 1-3 2.5z" fill="none" stroke="#0054AA" stroke-width="1.8"/></svg>
  <div class="abs btn nav-btn">Get SQF Consultation</div>
</header>

<!-- Hero -->
<div class="abs hero" role="img" aria-label="Food safety specialist reviewing a compliance checklist on a tablet inside a bright processing plant"></div>
<div class="abs hero-shade"></div>
<div class="abs hero-eyebrow">SQF ONLY · TECH DRIVEN</div>
<h1 class="abs serif hero-title">Hire a tech-driven<br>SQF team that carries you<br>across the certification<br>finish line.</h1>
<p class="abs hero-copy">At Northgate Assurance Group, we focus exclusively on SQF — combining real plant experience with smart technology so your team can stay focused on production while we handle the path to certification and beyond.</p>
<div class="abs btn hero-btn">Get SQF Consultation</div>

<!-- Stats -->
<svg class="abs stats-band" width="1200" height="190" viewBox="0 0 1200 190">
  <defs><linearGradient id="band" x1="0" x2="1"><stop offset="0" stop-color="#0054AA"/><stop offset="1" stop-color="#0677BA"/></linearGradient></defs>
  <path d="M0 0H1200V146H818L600 188L382 146H0Z" fill="url(#band)"/>
</svg>
<div class="abs stat-divider" style="left:403px"></div>
<div class="abs stat-divider" style="left:564px"></div>
<div class="abs stat-divider" style="left:803px"></div>
<div class="abs stat" style="left:194px"><div class="stat-num">15+</div><div class="stat-label">Clients Onboarded</div></div>
<div class="abs stat" style="left:379px"><div class="stat-num">100%</div><div class="stat-label">SQF Focused</div></div>
<div class="abs stat" style="left:577px"><div class="stat-num">DIGITAL</div><div class="stat-label">Platform Built Programs</div></div>
<div class="abs stat" style="left:798px"><div class="stat-num">US</div><div class="stat-label">Nationwide Coverage</div></div>

<!-- What we do -->
<div class="abs eyebrow center" style="top:952px">What we do</div>
<h2 class="abs serif section-title center" style="top:977px">SQF Consulting, Implementation<br>and Onboarding</h2>
<p class="abs lead center" style="top:1053px">We help food &amp; beverage manufacturers achieve &amp; maintain SQF certification with confidence, using practical<br>programs and digital tools that work on the floor — not just on audit day.</p>

<div class="abs card" style="left:113px">
  <svg width="66" height="74" viewBox="0 0 66 74"><path d="M33 2L64 16V50Q64 60 33 72Q2 60 2 50V16Z" fill="#0B2A5B"/><circle cx="33" cy="36" r="12" fill="none" stroke="#fff" stroke-width="2"/><circle cx="33" cy="36" r="5" fill="none" stroke="#fff" stroke-width="2"/></svg>
  <div class="card-title">SQF Program Design</div>
  <div class="card-text">We design your complete SQF system from scratch HACCP/food safety plans, prerequisite programs, SOPs, forms, logs, and all required documentation</div>
</div>
<div class="abs card" style="left:444px">
  <svg width="66" height="74" viewBox="0 0 66 74"><path d="M33 2L64 16V50Q64 60 33 72Q2 60 2 50V16Z" fill="#0054AA"/><rect x="20" y="26" width="26" height="18" rx="2" fill="none" stroke="#fff" stroke-width="2"/><path d="M17 48H49" stroke="#fff" stroke-width="2"/></svg>
  <div class="card-title">Digital Platform Build</div>
  <div class="card-text">We build your SQF program directly into modern food safety software like TraceLedger or SafeBatch — digitizing forms, checklists, monitoring.</div>
</div>
<div class="abs card" style="left:775px">
  <svg width="66" height="74" viewBox="0 0 66 74"><path d="M33 2L64 16V50Q64 60 33 72Q2 60 2 50V16Z" fill="#0B2A5B"/><rect x="21" y="24" width="24" height="22" rx="2" fill="none" stroke="#fff" stroke-width="2"/><path d="M26 31H40M26 37H40" stroke="#fff" stroke-width="2"/></svg>
  <div class="card-title">Coaching &amp; Support</div>
  <div class="card-text">After building your system, we coach your team to own and maintain it day-to-day. You run the program; we provide ongoing expert guidance.</div>
</div>
<div class="abs dots center" style="top:1384px"><span></span><span class="on"></span><span></span></div>

<!-- Why -->
<section class="abs why"></section>
<div class="abs eyebrow center" style="top:1537px">Why Northgate Assurance</div>
<h2 class="abs serif section-title center" style="top:1561px">Built for small and mid size<br>manufacturers</h2>
<p class="abs lead center" style="top:1639px">You don't need to hire a full-time food safety director or figure out SQF alone. We bring the<br>expertise and technology you stay focused on production.</p>

<svg class="abs" style="left:168px;top:1714px" width="342" height="396" viewBox="0 0 342 396" role="img" aria-label="Technician in protective clothing inspecting a bottling line with a tablet">
  <defs><linearGradient id="plant" x1="0" y1="0" x2="1" y2="1"><stop offset="0" stop-color="#dfe6ec"/><stop offset=".5" stop-color="#9aa8b5"/><stop offset="1" stop-color="#5e6b78"/></linearGradient></defs>
  <path d="M171 0L342 90V272Q342 332 171 396Q0 332 0 272V90Z" fill="#0677BA"/>
  <path d="M171 26L316 103V264Q316 314 171 370Q26 314 26 264V103Z" fill="#fff"/>
  <path d="M171 36L306 108V260Q306 306 171 358Q36 306 36 260V108Z" fill="url(#plant)"/>
</svg>

<div class="abs benefit" style="top:1767px">
  <div class="benefit-title"><svg width="13" height="13" viewBox="0 0 13 13"><circle cx="6.5" cy="6.5" r="6.5" fill="#2FA84F"/><path d="M3.5 6.7L5.7 8.8L9.6 4.6" fill="none" stroke="#fff" stroke-width="1.6"/></svg>Lower cost than a full-time hire</div>
  <div class="benefit-text">Get a complete SQF team — program design, digital implementation, and coaching — at a fraction of the cost of hiring a full-time SQF Practitioner.</div>
</div>
<div class="abs benefit" style="top:1846px">
  <div class="benefit-title"><svg width="13" height="13" viewBox="0 0 13 13"><circle cx="6.5" cy="6.5" r="6.5" fill="#2FA84F"/><path d="M3.5 6.7L5.7 8.8L9.6 4.6" fill="none" stroke="#fff" stroke-width="1.6"/></svg>Your program lives in software</div>
  <div class="benefit-text">No more binders and spreadsheets. Your SQF system is built into TraceLedger or SafeBatch — organized, accessible, and always audit-ready.</div>
</div>
<div class="abs benefit" style="top:1925px">
  <div class="benefit-title"><svg width="13" height="13" viewBox="0 0 13 13"><circle cx="6.5" cy="6.5" r="6.5" fill="#2FA84F"/><path d="M3.5 6.7L5.7 8.8L9.6 4.6" fill="none" stroke="#fff" stroke-width="1.6"/></svg>You own it, we support it</div>
  <div class="benefit-text">We build the system and train your team. You maintain and run it day-to-day. We stay on call with coaching and advisory so you never feel stuck.</div>
</div>
<div class="abs benefit" style="top:2004px">
  <div class="benefit-title"><svg width="13" height="13" viewBox="0 0 13 13"><circle cx="6.5" cy="6.5" r="6.5" fill="#2FA84F"/><path d="M3.5 6.7L5.7 8.8L9.6 4.6" fill="none" stroke="#fff" stroke-width="1.6"/></svg>Flexible, low-risk engagement</div>
  <div class="benefit-text">Start with a 3-month commitment, then go month-to-month. Cancel anytime with 30 days notice. We earn your business every month.</div>
</div>

<!-- How it works -->
<div class="abs eyebrow center" style="top:2265px">How it works</div>
<h2 class="abs serif section-title center" style="top:2289px">From discovery to certification</h2>
<p class="abs lead center" style="top:2330px">A clear, structured path that takes the guesswork out of SQF.</p>

<div class="abs step" style="left:182px">
  <svg width="66" height="74" viewBox="0 0 66 74"><path d="M33 2L64 16V50Q64 60 33 72Q2 60 2 50V16Z" fill="#0B2A5B"/><path d="M22 30Q33 20 44 30L41 34H25Z" fill="none" stroke="#fff" stroke-width="2"/><rect x="24" y="36" width="18" height="12" rx="2" fill="none" stroke="#fff" stroke-width="2"/></svg>
  <div class="card-title">Discovery Call</div>
  <div class="card-text">We learn about your facility, your current systems, &amp; where you are in the SQF journey No pressure — just a conversation.</div>
</div>
<div class="abs step step-featured" style="left:467px">
  <svg width="66" height="74" viewBox="0 0 66 74"><path d="M33 2L64 16V50Q64 60 33 72Q2 60 2 50V16Z" fill="#fff"/><rect x="22" y="24" width="20" height="24" rx="2" fill="none" stroke="#0054AA" stroke-width="2"/><circle cx="36" cy="40" r="6" fill="#fff" stroke="#0054AA" stroke-width="2"/></svg>
  <div class="card-title">Gap Assessment</div>
  <div class="card-text">We evaluate your facility against SQF requirements, identify what's missing, and give you a clear roadmap with priorities.</div>
</div>
<div class="abs step" style="left:751px">
  <svg width="66" height="74" viewBox="0 0 66 74"><path d="M33 2L64 16V50Q64 60 33 72Q2 60 2 50V16Z" fill="#0B2A5B"/><path d="M22 48V40H30V32H38V24H44" fill="none" stroke="#fff" stroke-width="2"/></svg>
  <div class="card-title">Build &amp; Implement</div>
  <div class="card-text">We design your SQF program &amp; build it directly into your digital food safety platform forms, logs, SOPs, HACCP plans, all of it.</div>
</div>
<div class="abs dots center" style="top:2647px"><span></span><span class="on"></span><span></span></div>

<!-- Testimonial -->
<div class="abs quote-mark center">&ldquo;</div>
<blockquote class="abs serif quote">Northgate Assurance Group didn't just hand us a binder. They built our entire SQF system into software and coached our team until we owned it. We passed our first audit with confidence.</blockquote>
<div class="abs stars center">★★★★★</div>
<div class="abs quote-by center">— SQF-CERTIFIED MANUFACTURING CLIENT</div>

<!-- CTA -->
<svg class="abs cta" width="1200" height="191" viewBox="0 0 1200 191">
  <defs><linearGradient id="ctag" x1="0" x2="1"><stop offset="0" stop-color="#0054AA"/><stop offset="1" stop-color="#0677BA"/></linearGradient></defs>
  <path d="M0 42H382L600 2L818 42H1200V191H0Z" fill="url(#ctag)"/>
</svg>
<h2 class="abs serif cta-title">Ready to talk SQF?</h2>
<p class="abs cta-copy">Share a few details about your facility and where you are in the SQF journey. We'll follow up with a brief discovery call and a clear next step.</p>
<div class="abs btn cta-btn">Get SQF Consultation</div>

<!-- Footer -->
<footer class="abs footer"></footer>
<div class="abs footer-base"></div>
<div class="abs brand footer-brand" style="left:115px;top:3402px">
  <span class="brand-dot" style="border-color:#0677BA;width:44px;height:44px"></span>
  <div>
    <div class="brand-name" style="font-size:20px">Northgate Assurance</div>
    <div class="brand-sub" style="color:#CADEEF;font-size:10px">FOOD SAFETY &amp; SQF CERTIFICATION</div>
  </div>
</div>
<p class="abs footer-about">Tech-driven SQF consulting for small and mid-size US food manufacturers. Based in Riverbend, CA — serving clients across North America.</p>

<div class="abs col-title" style="left:464px">Services</div>
<ul class="abs svc-list">
  <li><svg width="11" height="9" viewBox="0 0 11 9"><path d="M1 4.5L4 7.5L10 1" fill="none" stroke="#fff" stroke-width="1.6"/></svg>SQF Program Design</li>
  <li><svg width="11" height="9" viewBox="0 0 11 9"><path d="M1 4.5L4 7.5L10 1" fill="none" stroke="#fff" stroke-width="1.6"/></svg>Digital Platform Build</li>
  <li><svg width="11" height="9" viewBox="0 0 11 9"><path d="M1 4.5L4 7.5L10 1" fill="none" stroke="#fff" stroke-width="1.6"/></svg>Coaching &amp; Support</li>
  <li><svg width="11" height="9" viewBox="0 0 11 9"><path d="M1 4.5L4 7.5L10 1" fill="none" stroke="#fff" stroke-width="1.6"/></svg>Gap Assessments</li>
  <li><svg width="11" height="9" viewBox="0 0 11 9"><path d="M1 4.5L4 7.5L10 1" fill="none" stroke="#fff" stroke-width="1.6"/></svg>Sanitation Programs</li>
</ul>

<div class="abs col-title" style="left:697px">Connect</div>
<div class="abs contact" style="top:3403px">
  <div class="contact-head"><svg width="11" height="9" viewBox="0 0 11 9"><rect width="11" height="9" rx="1" fill="#fff"/><path d="M0.5 1L5.5 5L10.5 1" fill="none" stroke="#0B2A5B" stroke-width="1.2"/></svg>Email us</div>
  <div class="contact-text">hello@northgateassure.example</div>
</div>
<div class="abs contact" style="top:3451px">
  <div class="contact-head"><svg width="11" height="11" viewBox="0 0 11 11"><path d="M2 0.5L4.2 3L3 4.5Q4.5 7 6.5 8L8 6.8L10.5 9L9 10.5Q4 10 0.5 2Z" fill="#fff"/></svg>Phone</div>
  <div class="contact-text">(555) 014-2271</div>
</div>
<div class="abs contact" style="top:3499px">
  <div class="contact-head"><svg width="10" height="12" viewBox="0 0 10 12"><path d="M5 12Q0 6 0 4.5A5 5 0 0 1 10 4.5Q10 6 5 12Z" fill="#fff"/><circle cx="5" cy="4.5" r="1.7" fill="#0B2A5B"/></svg>Email address</div>
  <div class="contact-text">Reference site about Lorem Ipsum,<br>giving information on its origins,</div>
</div>

<div class="abs col-title" style="left:957px">Follow me</div>
<div class="abs social" style="left:960px;top:3409px"></div>
<div class="abs social" style="left:1001px;top:3409px"></div>
<div class="abs social" style="left:1041px;top:3409px"></div>
<div class="abs social" style="left:960px;top:3451px"></div>
<div class="abs social" style="left:1001px;top:3451px"></div>

<div class="abs copyright center">© 2026 Northgate Assurance Group LLC. All rights reserved. Created with Lumen Studio</div>
<div class="abs chat"><svg width="26" height="22" viewBox="0 0 26 22"><path d="M3 2H23Q25 2 25 4V14Q25 16 23 16H12L6 21V16H3Q1 16 1 14V4Q1 2 3 2Z" fill="#fff"/><circle cx="8" cy="9" r="1.6" fill="#0677BA"/><circle cx="13" cy="9" r="1.6" fill="#0677BA"/><circle cx="18" cy="9" r="1.6" fill="#0677BA"/></svg></div>

</body>
</html>
```